Website Front Page Banner Design for High Technology Intellectual Property

Develop Graphical Hero Banner to be used on the main page of Veltrona .com. The banner will promote the availability of Veltrona JESD204C IP (Intellectual Property). Please see attached pdf doc and follow details for Static Banner. We are looking for a Banner that is visually attention grabbing and uses imagery of applications that are enabled by the IP we are promoting (Applications such as 5G Wireless Infrastructure, CT/MRI/Ultrasound medical equipment, Radar / LIDAR / Satellites and High-Speed Test and Measurement equipment for a few examples). It would be good if the banner generally follow our color template of Green, White and Black - but the images of applications can use additional colors. Additonally, to learn more about JESD204 - recommend going to the following sites to understand what this IP is used for and what markets it address - additionally, I am open to answer any questions you may have. Sites: https://www.quarnify-tech.com/blog/high-speed-interface/jesd204c/, https://resources.pendrelo.com/p/what-jesd204c-standard-adcs,
Target Market(s)
Various High Technology Markets such as Defense, Medical, Test and Measurement, Industrial / Robotics, Wireless Communications
Industry/Entity Type
Semiconductor
Look and feel

```html
<!DOCTYPE html>
<html lang="en">
<head>
<meta charset="utf-8">
<title>Veltrona JESD204C IP Cores</title>
<link href="https://fonts.googleapis.com/css2?family=Jost:wght@100;200&family=Hind:wght@400&display=swap" rel="stylesheet">
<style>
  :root {
    --brand-green: #00b83f;
    --ink: #111111;
    --paper: #ffffff;
    --steel-light: #c9cbcb;
    --steel-dark: #8e918f;
  }
  html, body {
    margin: 0;
    padding: 0;
    width: 1200px;
    height: 720px;
    overflow: hidden;
    background: var(--paper);
  }
  .hero {
    position: relative;
    width: 1200px;
    height: 720px;
    overflow: hidden;
    background: var(--paper);
  }
  .hero__shapes {
    position: absolute;
    inset: 0;
  }
  .hero__shapes .accent { fill: var(--brand-green); }
  .hero__product-image {
    position: absolute;
    left: 0;
    top: 0;
  }
  .hero__copy {
    position: absolute;
    left: 128px;
    top: 0;
    width: 480px;
  }
  .hero__product {
    position: absolute;
    left: 2px;
    top: 88px;
    margin: 0;
    font-family: "Jost", sans-serif;
    font-weight: 200;
    font-size: 90px;
    line-height: 1;
    letter-spacing: -1px;
    color: var(--ink);
    white-space: nowrap;
  }
  .hero__category {
    position: absolute;
    left: 0;
    top: 177px;
    width: 435px;
    height: 114px;
    margin: 0;
    background: var(--brand-green);
    color: var(--paper);
    font-family: "Jost", sans-serif;
    font-weight: 100;
    font-size: 108px;
    line-height: 114px;
    letter-spacing: -1px;
    text-indent: 10px;
    overflow: hidden;
    white-space: nowrap;
  }
  .hero__text {
    position: absolute;
    left: 3px;
    top: 300px;
    width: 432px;
    margin: 0;
    font-family: "Hind", sans-serif;
    font-weight: 400;
    font-size: 19px;
    line-height: 31px;
    color: var(--ink);
  }
  .hero__cta {
    position: absolute;
    left: 3px;
    top: 447px;
    width: 187px;
    height: 52px;
    border-radius: 26px;
    background: var(--brand-green);
    color: var(--paper);
    font-family: "Hind", sans-serif;
    font-size: 20px;
    line-height: 55px;
    text-align: center;
    text-decoration: none;
  }
</style>
</head>
<body>
  <main class="hero">
    <svg class="hero__shapes" width="1200" height="720" viewBox="0 0 1200 720" aria-hidden="true">
      <path class="accent" d="M752 0 L1200 0 L1200 546 C1150 470 1085 420 1000 385 C860 300 768 160 752 0 Z"/>
      <polygon class="accent" points="0,414 128,600 128,720 0,720"/>
      <polygon class="accent" points="0,414 128,600 0,600" transform="translate(0,0)"/>
    </svg>

    <svg class="hero__product-image" width="1200" height="720" viewBox="0 0 1200 720" role="img" aria-label="Photograph of a large satellite dish antenna on a steel lattice tower, tilted up toward the upper right">
      <defs>
        <linearGradient id="steel" x1="0" y1="0" x2="1" y2="1">
          <stop offset="0" stop-color="#c9cbcb" stop-opacity="0.85"/>
          <stop offset="1" stop-color="#8e918f" stop-opacity="0.85"/>
        </linearGradient>
      </defs>
      <rect x="620" y="65" width="506" height="655" fill="url(#steel)"/>
    </svg>

    <section class="hero__copy">
      <h1 class="hero__product">JESD204C</h1>
      <h2 class="hero__category">IP Cores</h2>
      <p class="hero__text">Veltrona JESD204C IP links high-speed data converters for 5G radios, medical imaging, radar, LIDAR, satellites and test equipment with proven, low-latency serial lanes.</p>
      <a class="hero__cta" href="#">Learn More</a>
    </section>
  </main>
</body>
</html>
```